RK Bastone Construction Inc.

Design a new business card for our construction company
To be removed from current card:
Delete 25 years
Delete Tenant fit up Renovations section

```html
<!DOCTYPE html>
<html lang="en">
<head>
<meta charset="utf-8">
<title>RK Bastone Construction Inc. – Business Card</title>
<link href="https://fonts.googleapis.com/css2?family=Archivo:wght@700;800&family=Poppins:wght@300;400;600&family=Rubik:wght@500;700&display=swap" rel="stylesheet">
<style>
  :root {
    --purple: #55297a;
    --teal: #227a6e;
    --ink: #222222;
    --card: #ffffff;
    --backdrop: #e8e3da;
  }
  * { box-sizing: border-box; margin: 0; padding: 0; }
  html, body { width: 900px; height: 1200px; overflow: hidden; }
  body {
    background: var(--backdrop);
    position: relative;
    font-family: "Poppins", sans-serif;
  }
  .card {
    position: absolute;
    left: 82px;
    width: 735px;
    height: 428px;
    background: var(--card);
    border-radius: 22px;
    overflow: hidden;
    box-shadow: 0 3px 10px rgba(0,0,0,0.18);
  }
  .card--front { top: 126px; }
  .card--back { top: 637px; }

  .company-name {
    font-family: "Poppins", sans-serif;
    font-weight: 600;
    color: var(--purple);
    text-transform: uppercase;
    font-size: 34px;
    line-height: 1.05;
    letter-spacing: 0.5px;
  }
  .card--front .company-name { position: absolute; left: 48px; top: 56px; }
  .card--back .company-name {
    position: absolute; left: 0; right: 0; top: 178px; text-align: center;
  }

  .holder-name {
    position: absolute; left: 48px; top: 218px;
    font-family: "Archivo", sans-serif; font-weight: 800;
    font-size: 21px; letter-spacing: 0.5px; color: var(--purple);
  }
  .holder-name .surname { color: var(--teal); }
  .holder-title {
    position: absolute; left: 48px; top: 244px;
    font-weight: 300; font-size: 17px; letter-spacing: 1px; color: var(--purple);
  }
  .name-rule {
    position: absolute; left: 48px; top: 274px; width: 430px; height: 2px;
    background: var(--teal);
  }
  .mobile-tab { position: absolute; left: 461px; top: 242px; width: 227px; height: 34px; }
  .mobile-tab .tab-shape { position: absolute; left: 0; top: 0; width: 227px; height: 34px; }
  .mobile-tab .mobile-number {
    position: absolute; right: 10px; top: 0; height: 34px;
    font-family: "Rubik", sans-serif; font-weight: 700; font-size: 20px;
    letter-spacing: 1px; color: #fff;
    display: flex; align-items: center; gap: 7px;
  }
  .mobile-tab .mobile-icon { width: 12px; height: 18px; flex: none; display: block; }

  .contact-list {
    position: absolute; left: 48px; top: 287px; list-style: none;
    font-size: 16px; color: var(--ink);
  }
  .contact-list li { display: flex; align-items: center; gap: 10px; height: 25px; }
  .contact-list svg { width: 18px; height: 18px; flex: none; }

  .address {
    position: absolute; right: 47px; top: 287px; text-align: right;
    font-style: normal; font-size: 16px; color: var(--ink); line-height: 25px;
  }

  .footer-bands { position: absolute; left: 0; top: 394px; width: 735px; height: 34px; }
  .sectors {
    position: absolute; right: 47px; top: 402px;
    font-family: "Rubik", sans-serif; font-weight: 500; font-size: 14px;
    letter-spacing: 1.3px; color: #fff; text-transform: uppercase;
  }
  .sectors .divider { margin: 0 7px; opacity: 0.9; }

  .back-url {
    position: absolute; left: 0; right: 0; top: 375px; text-align: center;
    font-size: 16px; letter-spacing: 5.5px; color: var(--teal); text-transform: uppercase;
  }
</style>
</head>
<body>

<section class="card card--front" aria-label="Business card front">
  <div class="company-name">RK Bastone<br>Construction Inc.</div>

  <div class="holder-name">MARCO <span class="surname">BASTONE</span></div>
  <div class="holder-title">OWNER</div>
  <div class="name-rule"></div>

  <div class="mobile-tab">
    <svg class="tab-shape" viewBox="0 0 227 34" preserveAspectRatio="none" aria-hidden="true">
      <polygon points="18,0 227,0 227,34 0,34" fill="var(--teal)"/>
    </svg>
    <span class="mobile-number">
      <svg class="mobile-icon" viewBox="0 0 12 18" aria-hidden="true"><rect x="1" y="1" width="10" height="16" rx="2" fill="none" stroke="#fff" stroke-width="2"/><circle cx="6" cy="14" r="1" fill="#fff"/></svg>
      <span>555-214-7730</span>
    </span>
  </div>

  <ul class="contact-list">
    <li>
      <svg viewBox="0 0 24 24"><path d="M6.6 10.8a15 15 0 0 0 6.6 6.6l2.2-2.2a1 1 0 0 1 1-.25 11.4 11.4 0 0 0 3.6.57 1 1 0 0 1 1 1V20a1 1 0 0 1-1 1A17 17 0 0 1 3 4a1 1 0 0 1 1-1h3.5a1 1 0 0 1 1 1c0 1.25.2 2.45.57 3.57a1 1 0 0 1-.25 1z" fill="var(--teal)"/></svg>
      555-380-4412 ext. 221
    </li>
    <li>
      <svg viewBox="0 0 24 24"><rect x="2" y="5" width="20" height="14" fill="var(--teal)"/><polyline points="2,5 12,13 22,5" fill="none" stroke="#fff" stroke-width="1.6"/></svg>
      marco@rkbastoneconst.ca
    </li>
    <li>
      <svg viewBox="0 0 24 24" fill="none" stroke="var(--teal)" stroke-width="1.8"><circle cx="12" cy="12" r="9"/><ellipse cx="12" cy="12" rx="4" ry="9"/><line x1="3" y1="12" x2="21" y2="12"/></svg>
      www.rkbastoneconstruction.ca
    </li>
  </ul>

  <address class="address">
    1280 Fieldstone Rd<br>
    Suite 100, Ottawa<br>
    ON K2X 4R7
  </address>

  <svg class="footer-bands" viewBox="0 0 735 34" aria-hidden="true">
    <polygon points="0,1 398,1 382,17 0,17" fill="var(--teal)"/>
    <polygon points="408,0 735,0 735,34 0,34 0,24 385,24" fill="var(--purple)"/>
  </svg>
  <div class="sectors">Office<span class="divider">|</span>Retail<span class="divider">|</span>Institutional</div>
</section>

<section class="card card--back" aria-label="Business card back">
  <div class="company-name">RK Bastone<br>Construction Inc.</div>
  <div class="back-url">www.rkbastoneconstruction.ca</div>
</section>

</body>
</html>
```